" Window Blinds and Shutters Business Card Design"

We require a business card design for a new windows blinds and shutters company based in Sydney.
The business name is 'Larkvale Blinds and Shutters'.
We supply and install homes and businesses with internal and external window furnishings and finishes. This includes varieties of window blinds and window shutters.

Benefits of Larkvale Blinds and Shutters :
Added security and privacy,
The ability to control the amount of sunlight,
Regulate internal temperature.

Blinds varieties:
Roller Blinds, Double Roller Blinds, Roman Blinds, Vertical Blinds, Aluminium venetians, Timber venetians and PVC Venetians.

Shutters varieties:
Plantation Shutters, Aluminium Louvre Shutters, Roller Shutters and Security Shutters .
Updates

Hi Designers,

Please have a look at my Business card design brief. I need your help to start my new business.

Thanks,

Dorian.

Reason: not 100% happy with the options available, close to 90% happy, need a little more refinement. Thank You & Good Luck

Target Market(s)

Home owners, business owners, shift workers , and new home builders.

Industry/Entity Type

Security

Contact Information for Business Card

Larkvale Blinds and Shutters,

Dorian Kettlewell mobile: 0487561904,
Priya Hensworth mobile: 0472846015,

email: dorian.kettlewell@mailgrove.net
web: larkvaleblindsandshutters.com.au

Colors
ffffff
9d9d9d
f78f20

Requirements
Must have
• ON FRONT OF CARD
I have attached a picture of logo and need a designer to design a font logo for Larkvale Blinds and Shutters similar, or open to suggestions.

FRONT OF CARD
Company message/:
"Safeguarding windows by design"

BACK OF CARD
'For a FREE measure & quote call Dorian - 0487561904"
Nice to have
• Elegant yet professional.

Soft colours appealing to both male & female clients.

Should not have

• Unprofessional fonts

```html
<!DOCTYPE html>
<html lang="en">
<head>
<meta charset="utf-8">
<title>Larkvale Blinds and Shutters – Business Card</title>
<link rel="stylesheet" href="https://fonts.googleapis.com/css2?family=Arimo:wght@400&family=Oswald:wght@300&display=swap">
<style>
  :root {
    --silk-deep: #2f6a4f;
    --silk-mid: #8fb5a2;
    --silk-light: #eef5f1;
    --card-white: #ffffff;
    --band-purple: #5b2a6e;
    --band-red: #d2353a;
    --ink: #1a1a1a;
    --ink-soft: #2a2a2a;
    --link: #3b55c9;
    --mark-grey: #9d9d9d;
    --edge: #555555;
  }
  * { margin: 0; padding: 0; box-sizing: border-box; }
  html, body { width: 1200px; height: 841px; overflow: hidden; }
  body { position: relative; font-family: "Arimo", Arial, sans-serif; color: var(--ink); }

  .silk-backdrop {
    position: absolute; inset: 0;
    background:
      linear-gradient(90deg,
        var(--silk-mid) 0%, var(--silk-light) 6%, var(--silk-mid) 12%, var(--silk-light) 18%,
        var(--silk-mid) 26%, var(--silk-light) 34%, var(--silk-mid) 42%, var(--silk-light) 50%,
        var(--silk-mid) 58%, var(--silk-light) 64%, var(--silk-mid) 72%, var(--silk-light) 80%,
        var(--silk-mid) 88%, var(--silk-deep) 100%);
  }

  /* Front of card */
  .card-front {
    position: absolute; left: 88px; top: 80px; width: 580px; height: 336px;
    border: 1px solid var(--edge);
    background: var(--card-white);
  }
  .brand-mark {
    position: absolute; left: 50%; top: 26px; width: 100px; height: 100px;
    margin-left: -50px; border-radius: 50%; background: var(--mark-grey);
  }
  .name-band {
    position: absolute; left: 0; right: 0; top: 168px; bottom: 0;
    background: linear-gradient(90deg, var(--band-purple), var(--band-red));
  }
  .brand-name {
    position: absolute; font-weight: 400; color: var(--ink); line-height: 1; white-space: nowrap;
  }
  .brand-name.line-one { left: 43px; top: 22px; font-size: 36px; }
  .brand-name.line-two { left: 324px; top: 58px; font-size: 36px; }
  .brand-name.line-three { left: 363px; top: 87px; font-size: 45px; }

  /* Back of card */
  .card-back {
    position: absolute; left: 593px; top: 478px; width: 580px; height: 337px;
    border: 1px solid var(--edge);
    background: linear-gradient(180deg, var(--band-purple), var(--band-red));
  }
  .benefits {
    position: absolute; left: 35px; top: 28px;
    font-family: "Oswald", "Arial Narrow", sans-serif; font-weight: 300;
    font-size: 14.5px; line-height: 22px; color: var(--ink-soft);
  }
  .benefits h3 { font-weight: 300; font-size: 14.5px; text-decoration: underline; }
  .benefits ul, .varieties-shutters ul { list-style: none; }
  .varieties-shutters {
    position: absolute; left: 322px; top: 25px; font-size: 16px; line-height: 19px;
  }
  .varieties-shutters h3 { font-weight: 400; font-size: 16px; }
  .varieties-shutters li { padding-left: 16px; text-indent: -16px; }
  .varieties-blinds {
    position: absolute; left: 0; right: 0; top: 126px; text-align: center; font-size: 15px; line-height: 19px;
  }
  .varieties-blinds h3 { font-weight: 400; font-size: 18px; line-height: 22px; }
  .divider {
    position: absolute; left: 20px; right: 18px; top: 206px; height: 5px;
    background: var(--ink); border-radius: 3px;
  }
  .contact {
    position: absolute; left: 0; right: 0; top: 219px; text-align: center;
  }
  .contact .company { font-size: 21px; line-height: 26px; }
  .contact .person { font-size: 13px; line-height: 21px; margin-top: 4px; }
  .contact .person + .person { margin-top: 0; }
  .contact .online { font-size: 13px; line-height: 17px; margin-top: 10px; }
  .contact .online a { color: var(--link); }
</style>
</head>
<body>
  <div class="silk-backdrop" role="img" aria-label="Flowing green and white silk drapery background"></div>

  <section class="card-front">
    <span class="brand-mark" aria-hidden="true"></span>
    <div class="name-band">
      <span class="brand-name line-one">Larkvale Blinds</span>
      <span class="brand-name line-two">and</span>
      <span class="brand-name line-three">Shutters</span>
    </div>
  </section>

  <section class="card-back">
    <div class="benefits">
      <h3>Benefits of Larkvale Blinds and Shutters :</h3>
      <ul>
        <li>&gt; Added security and privacy</li>
        <li>&gt; The ability to control the amount of sunlight</li>
        <li>&gt; Regulate internal temperature</li>
      </ul>
    </div>
    <div class="varieties-shutters">
      <h3>Blinds varieties:</h3>
      <ul>
        <li>&gt; Plantation Shutters</li>
        <li>&gt; Aluminium Louvre Shutters</li>
        <li>&gt; Roller Shutters and Security Shutters</li>
      </ul>
    </div>
    <div class="varieties-blinds">
      <h3>Blinds varieties:</h3>
      <p>Roller Blinds, Double Roller Blinds, Roman Blinds, Vertical Blinds,<br>Aluminium venetians, Timber venetians and PVC Venetians.</p>
    </div>
    <div class="divider"></div>
    <div class="contact">
      <p class="company">Larkvale Blinds and Shutters</p>
      <p class="person">Dorian Kettlewell mobile: 0487561904</p>
      <p class="person">Priya Hensworth mobile: 0472846015</p>
      <p class="online">Business Partners email: <a href="mailto:dorian.kettlewell@mailgrove.net">dorian.kettlewell@mailgrove.net</a><br>web: larkvaleblindsandshutters.com.au</p>
    </div>
  </section>
</body>
</html>
```